Bed Company needs business card

Hello, we are a bed company that makes specialized magnets for beds. We are an alternative healing company. I need a modern and upscale business card. Please incorporate my logo for the card.

Accepted file formats are AI, EPS, and Press-Ready PDFS.

Please include all fonts or convert them to outlines regardless of file type.

If you are designing the card in Photoshop the file Must be 1200dpi.

I am open to anything for the business card.  I really like all of your designs and if you want to change the color of the logo, you can.  I will be making the final selection by Friday.  Thank You for all of your designs.  Feel Free to submit different color logos if you want.  

Reason: I will make a decision Final on Friday April 20th. 2012. Good Luck and Thank you all for the designs.

Target Market(s)

My target Market is people, who are looking for alternative healing.

Industry/Entity Type

Business

Requirements
Must have
• My logo must be incorporated. The front card must have

Name
Job Title

Address
Work
Cell
Fax
email
web

Just put in fake info for the card.

The back of the card. I want the logo on the back with color. I just want it to look modern and cool.

```html
<!DOCTYPE html>
<html lang="en">
<head>
<meta charset="utf-8">
<title>Lodestone Rest – Business Card</title>
<link href="https://fonts.googleapis.com/css2?family=Montserrat:wght@400;500;700&display=swap" rel="stylesheet">
<style>
  :root {
    --bg: #ece9e4;
    --card: #ffffff;
    --green-dark: #08643a;
    --green-bright: #12913f;
    --green-text: #0b6b36;
    --ink: #3a3a3a;
  }
  html, body {
    margin: 0;
    width: 1200px;
    height: 1200px;
    overflow: hidden;
    background: var(--bg);
    font-family: "Montserrat", Arial, sans-serif;
  }
  .card {
    position: absolute;
    left: 205px;
    width: 790px;
    height: 440px;
    border-radius: 14px;
    background: linear-gradient(180deg, #fbfbfb 0%, #ffffff 40%, #f1f1f1 100%);
    overflow: hidden;
    box-shadow: 0 2px 6px rgba(0,0,0,0.18);
  }
  .card--front { top: 150px; }
  .card--back { top: 615px; }
  .swoosh { position: absolute; left: 0; top: 0; width: 790px; height: 440px; }

  .brand { position: absolute; display: flex; align-items: center; color: var(--green-bright); font-weight: 700; }
  .brand__square { background: var(--green-dark); }
  .card--front .brand { left: 78px; top: 100px; font-size: 40px; gap: 16px; }
  .card--front .brand__square { width: 34px; height: 34px; }
  .card--back .brand { left: 0; right: 0; top: 195px; justify-content: center; font-size: 62px; gap: 24px; }
  .card--back .brand__square { width: 52px; height: 52px; }

  .person { position: absolute; right: 77px; top: 118px; text-align: right; }
  .person__name { font-size: 23px; font-weight: 500; color: var(--green-text); line-height: 28px; }
  .person__title { font-size: 16px; color: var(--ink); line-height: 22px; }

  .address { position: absolute; left: 78px; top: 268px; font-size: 17px; line-height: 24px; color: var(--ink); }
  .address__company { color: var(--green-text); font-weight: 500; }

  .contact { position: absolute; right: 70px; top: 244px; list-style: none; margin: 0; padding: 0; }
  .contact li { display: flex; align-items: center; justify-content: flex-end; gap: 14px; font-size: 17px; line-height: 24px; color: var(--ink); }
  .contact svg { width: 20px; height: 18px; fill: var(--green-dark); }
</style>
</head>
<body>

<section class="card card--front">
  <svg class="swoosh" viewBox="0 0 790 440" aria-hidden="true">
    <path d="M0,342 Q400,470 790,326 L790,362 Q400,478 0,350 Z" fill="var(--green-bright)"/>
    <path d="M0,357 Q400,484 790,370 L790,440 L0,440 Z" fill="var(--green-dark)"/>
  </svg>

  <div class="brand"><span class="brand__square"></span>Lodestone Rest</div>

  <div class="person">
    <div class="person__name">Marcus Ellery</div>
    <div class="person__title">Chief Executive Officer</div>
  </div>

  <div class="address">
    <div class="address__company">Lodestone Rest, Inc</div>
    <div>4870 E Cedar Ridge Rd</div>
    <div>Mesa, Arizona 85215</div>
  </div>

  <ul class="contact">
    <li>1-480-555-0142
      <svg viewBox="0 0 20 18"><path d="M2 6 Q10 0 18 6 L16 8 L13 6 L13 4 Q10 3 7 4 L7 6 L4 8 Z M5 9 L15 9 L17 16 L3 16 Z"/></svg></li>
    <li>1-480-555-0187
      <svg viewBox="0 0 20 18"><rect x="5" y="1" width="10" height="6"/><rect x="2" y="7" width="16" height="9" rx="1"/><rect x="5" y="10" width="10" height="1.5" fill="#fff"/><rect x="5" y="13" width="10" height="1.5" fill="#fff"/></svg></li>
    <li>marcus@lodestonerest.com
      <svg viewBox="0 0 20 18"><path d="M2 3 H18 V15 H2 Z M3.5 4.5 V13.5 H16.5 V4.5 L10 10 Z" fill-rule="evenodd"/></svg></li>
    <li>www.lodestonerest.com
      <svg viewBox="0 0 20 18"><circle cx="10" cy="9" r="8"/><path d="M6 5 Q9 4 10 7 Q8 9 6 8 Z M11 10 Q15 10 14 14 Q11 13 11 10 Z" fill="#fff" opacity="0.5"/></svg></li>
  </ul>
</section>

<section class="card card--back">
  <svg class="swoosh" viewBox="0 0 790 440" aria-hidden="true">
    <path d="M0,345 Q400,470 790,326 L790,360 Q400,478 0,352 Z" fill="var(--green-bright)"/>
    <path d="M0,360 Q400,484 790,368 L790,440 L0,440 Z" fill="var(--green-dark)"/>
  </svg>

  <div class="brand"><span class="brand__square"></span>Lodestone Rest</div>
</section>

</body>
</html>
```